Quillet Studios business card

Front of card should be logo and back of card should be communication info.
Please note: reverse the logo color. Card should be black and everything else white.

Industry/Entity Type

Custom home design/construction

Contact Information for Business Card

Quillet Studios, LLC 555-382-0146 quilletstudios@mailbox-example.com

Requirements
Must have
• Square card, Logo on front, communication info on back and perhaps a mini version of the logo on back also. Black card/white lettering. Double sides square card.
Nice to have
• I want to keep it simple. Our product (custom homes) speak for themselves.

```html
<!DOCTYPE html>
<html lang="en">
<head>
<meta charset="utf-8">
<title>Quillet Studios business card</title>
<link href="https://fonts.googleapis.com/css2?family=Montserrat:wght@300;400;600&display=swap" rel="stylesheet">
<style>
  :root {
    --backdrop: #686768;
    --card-black: #222222;
    --card-white: #ffffff;
    --ink-light: #f2f2f2;
    --ink-dark: #1f1f1f;
  }
  * { margin: 0; padding: 0; box-sizing: border-box; }
  html, body {
    width: 1200px; height: 900px; overflow: hidden;
    background: var(--backdrop);
    font-family: "Montserrat", Arial, sans-serif;
  }
  .card {
    position: absolute;
    border-radius: 24px;
    overflow: hidden;
  }
  .card-back {
    left: 133px; top: 253px; width: 403px; height: 401px;
    background: var(--card-white);
  }
  .card-front {
    left: 602px; top: 236px; width: 429px; height: 428px;
    background: var(--card-black);
  }
  .back-band {
    position: absolute; left: 0; top: 0; width: 100%; height: 100%;
  }
  .brand-name {
    position: absolute; left: 0; width: 100%;
    text-align: center;
    font-weight: 600;
    text-transform: uppercase;
    letter-spacing: 0.5px;
  }
  .card-back .brand-name {
    top: 115px; font-size: 24px; color: var(--ink-dark);
  }
  .card-front .brand-name {
    top: 196px; font-size: 30px; color: var(--ink-light);
  }
  .holder {
    position: absolute; left: 0; width: 100%; text-align: center;
    color: var(--ink-light);
  }
  .holder-name { top: 224px; font-size: 21px; font-weight: 600; }
  .holder-title { top: 251px; font-size: 14px; font-weight: 300; }
  .icon-rule {
    position: absolute; left: 103px; top: 280px; width: 200px; height: 18px;
  }
  .contact-list {
    position: absolute; left: 0; top: 315px; width: 100%;
    list-style: none; text-align: center;
    color: var(--ink-light); font-size: 13.5px; font-weight: 300;
    line-height: 22px;
  }
</style>
</head>
<body>
  <section class="card card-back" aria-label="Card back with contact details">
    <svg class="back-band" viewBox="0 0 403 401" aria-hidden="true">
      <path d="M0 229 Q201 174 403 229 L403 401 L0 401 Z" fill="var(--card-black)"/>
    </svg>
    <div class="brand-name">Quillet Studios</div>
    <div class="holder holder-name">Dara Whitlow</div>
    <div class="holder holder-title">CEO &amp; Founder</div>
    <svg class="icon-rule" viewBox="0 0 200 18" aria-hidden="true">
      <line x1="0" y1="9" x2="63" y2="9" stroke="#f2f2f2" stroke-width="1.5"/>
      <line x1="137" y1="9" x2="200" y2="9" stroke="#f2f2f2" stroke-width="1.5"/>
      <rect x="69" y="1" width="16" height="16" rx="3" fill="#f2f2f2"/>
      <path d="M72.5 11 Q77 5 81.5 11 L80.5 13 L73.5 13 Z" fill="none" stroke="#222" stroke-width="1.3"/>
      <rect x="92" y="1" width="16" height="16" rx="3" fill="#f2f2f2"/>
      <rect x="94.5" y="5" width="11" height="8" fill="none" stroke="#222" stroke-width="1.2"/>
      <path d="M94.5 5 L100 9.5 L105.5 5" fill="none" stroke="#222" stroke-width="1.2"/>
      <rect x="115" y="1" width="16" height="16" rx="3" fill="#f2f2f2"/>
      <circle cx="123" cy="9" r="5" fill="none" stroke="#222" stroke-width="1.3"/>
      <path d="M118 9 H128 M123 4 Q120 9 123 14 Q126 9 123 4" fill="none" stroke="#222" stroke-width="1"/>
    </svg>
    <ul class="contact-list">
      <li>555 382 0146</li>
      <li>quilletstudios@mailbox-example.com</li>
      <li>www.quilletstudios-example.com</li>
    </ul>
  </section>

  <section class="card card-front" aria-label="Card front with company name">
    <div class="brand-name">Quillet Studios</div>
  </section>
</body>
</html>
```